Graphic to show easy steps to find financial clarity

Howdy-I need a graphic that describe my Coin Harbor Method.The attached is a concept, but please use your own creativity to show how you would display this:- There are 5 steps the process (and then we repeat/recalculate)- And three bullets that drive home the results of the processI've also attached my logo. Please use the colors in my logo and maybe add a soft green as needed.The reader should be able to briefly scan this document and understand that this is an easy/simple process that tells them how to manage their cash.Thanks!-Ned

Target Market(s)

wealthy women, whether single or married

Requirements
Must have
• Please use the colors in my logo and a soft green if needed
Should not have
• This should be a very easy to read graphic that communicates how simple/easy this is to do.

```html
<!DOCTYPE html>
<html lang="en">
<head>
<meta charset="utf-8">
<title>Coin Harbor Method</title>
<link href="https://fonts.googleapis.com/css2?family=Source+Sans+3:wght@400;500&family=Open+Sans:wght@400&display=swap" rel="stylesheet">
<style>
  :root {
    --navy: #1f3a70;
    --slate: #646262;
    --green-top: #cce4cf;
    --green-bottom: #f5f9f5;
    --page: #ffffff;
    --label: #ffffff;
  }
  html, body {
    margin: 0;
    padding: 0;
    width: 1200px;
    height: 800px;
    overflow: hidden;
    background: var(--page);
  }
  .canvas {
    position: relative;
    width: 1200px;
    height: 800px;
  }
  .method-panel {
    position: absolute;
    left: 244px;
    top: 91px;
    width: 720px;
    height: 607px;
    background: linear-gradient(to bottom, var(--green-top), var(--green-bottom));
  }
  .method-title {
    position: absolute;
    left: 0;
    top: 40px;
    width: 720px;
    margin: 0;
    text-align: center;
    font-family: "Source Sans 3", sans-serif;
    font-weight: 500;
    font-size: 45px;
    letter-spacing: 9px;
    color: var(--navy);
    line-height: 1;
  }
  .step-list {
    position: absolute;
    left: 60px;
    top: 122px;
    margin: 0;
    padding: 0;
    list-style: none;
  }
  .step {
    position: relative;
    width: 600px;
    height: 41px;
  }
  .step-tag {
    position: absolute;
    left: 0;
    top: 0;
    width: 164px;
    height: 35px;
  }
  .step-tag polygon { fill: var(--navy); }
  .step--alt .step-tag polygon { fill: var(--slate); }
  .step-label {
    position: absolute;
    left: 20px;
    width: 118px;
    top: 0;
    height: 35px;
    line-height: 35px;
    text-align: right;
    font-family: "Source Sans 3", sans-serif;
    font-size: 27px;
    color: var(--label);
    letter-spacing: 0.5px;
    white-space: nowrap;
  }
  .step-text {
    position: absolute;
    left: 187px;
    top: 0;
    height: 35px;
    line-height: 35px;
    font-family: "Open Sans", sans-serif;
    font-size: 25px;
    letter-spacing: 0.6px;
    color: var(--navy);
    white-space: nowrap;
  }
  .step--alt .step-text { color: var(--slate); }
  .step-rule {
    position: absolute;
    left: 164px;
    top: 37px;
    width: 435px;
    height: 1px;
    background: var(--navy);
  }
  .outcome-list {
    position: absolute;
    left: 63px;
    top: 402px;
    width: 585px;
    margin: 0;
    padding: 0;
    list-style: none;
    font-family: "Source Sans 3", sans-serif;
    font-size: 28px;
    line-height: 31px;
    color: var(--navy);
    text-transform: uppercase;
  }
  .outcome {
    position: relative;
    padding-left: 20px;
  }
  .outcome::before {
    content: "";
    position: absolute;
    left: 0;
    top: 12px;
    width: 9px;
    height: 9px;
    border-radius: 50%;
    background: var(--navy);
  }
</style>
</head>
<body>
<div class="canvas">
  <section class="method-panel">
    <h1 class="method-title">COIN HARBOR METHOD</h1>

    <ol class="step-list">
      <li class="step">
        <svg class="step-tag" viewBox="0 0 164 35" aria-hidden="true"><polygon points="0,0 157,0 164,17.5 157,35 0,35 8,17.5"/></svg>
        <span class="step-label">STEP 1</span>
        <span class="step-text">Know your annual spending</span>
        <span class="step-rule"></span>
      </li>
      <li class="step step--alt">
        <svg class="step-tag" viewBox="0 0 164 35" aria-hidden="true"><polygon points="0,0 157,0 164,17.5 157,35 0,35 8,17.5"/></svg>
        <span class="step-label">STEP 2</span>
        <span class="step-text">Project special expenses</span>
        <span class="step-rule"></span>
      </li>
      <li class="step">
        <svg class="step-tag" viewBox="0 0 164 35" aria-hidden="true"><polygon points="0,0 157,0 164,17.5 157,35 0,35 8,17.5"/></svg>
        <span class="step-label">STEP 3</span>
        <span class="step-text">Add up your 5-year cash needs</span>
        <span class="step-rule"></span>
      </li>
      <li class="step step--alt">
        <svg class="step-tag" viewBox="0 0 164 35" aria-hidden="true"><polygon points="0,0 157,0 164,17.5 157,35 0,35 8,17.5"/></svg>
        <span class="step-label">STEP 4</span>
        <span class="step-text">Set them aside in savings</span>
        <span class="step-rule"></span>
      </li>
      <li class="step">
        <svg class="step-tag" viewBox="0 0 164 35" aria-hidden="true"><polygon points="0,0 157,0 164,17.5 157,35 0,35 8,17.5"/></svg>
        <span class="step-label">STEP 5</span>
        <span class="step-text">Invest the rest</span>
        <span class="step-rule"></span>
      </li>
      <li class="step step--alt">
        <svg class="step-tag" viewBox="0 0 164 35" aria-hidden="true"><polygon points="0,0 157,0 164,17.5 157,35 0,35 8,17.5"/></svg>
        <span class="step-label">REPEAT</span>
        <span class="step-text">Recalculate monthly</span>
      </li>
    </ol>

    <ul class="outcome-list">
      <li class="outcome">Know your lifestyle will be unaffected by the markets for at least 5 years</li>
      <li class="outcome">Spend intentionally and with joy</li>
      <li class="outcome">Create a solid base for lifetime cash projections</li>
    </ul>
  </section>
</div>
</body>
</html>
```